Judicial election website to attract voters

I need a simple one-page web design for a judicial election. I'm going to put up one picture, maybe two. The picture I have needs a little touch-up (whiten teeth for example). I have 3 paragraphs of text. I'd like a "Donate" button that can link to a CoinDrift account. I'd also like a little background design, like the Constitution or something like that. There's a couple other little things but that's the bulk of it.

Target Market(s)

Involved voters and some media

Industry/Entity Type

Legal

Number of Pages Required

1 page

Font styles to use
Sans Serif

Requirements
Must have
• My picture, text, donate button
• Phrase "Remember to vote August 30, 2016!"
Nice to have
• Perhaps a second photo, maybe a short 30 second video of me talking directly to the voters, cool background: Constitution, something judgey.
Should not have
• Not sure ... profanity, I guess.

```html
<!DOCTYPE html>
<html lang="en">
<head>
<meta charset="utf-8">
<title>Maribel Catherine Van Horn for Circuit Court Judge</title>
<link rel="stylesheet" href="https://fonts.googleapis.com/css2?family=Crimson+Pro:ital,wght@0,400;0,600;0,700;1,700&family=Crimson+Text:wght@400;600;700&family=Roboto+Condensed:wght@400;700&display=swap">
<style>
  :root {
    --blue: #0d3a9e;
    --ink: #1d1d1d;
    --paper-light: #ececec;
    --paper-mid: #cfcfcf;
    --paper-dark: #a9a9a9;
    --band: #8d1c24;
    --donate-top: #e2312c;
    --donate-bottom: #a4130f;
  }
  * { margin: 0; padding: 0; box-sizing: border-box; }
  html, body { width: 896px; height: 1200px; overflow: hidden; background: var(--paper-mid); }
  .page {
    position: relative; width: 896px; height: 1200px; overflow: hidden;
    font-family: "Crimson Text", Georgia, serif; color: var(--ink);
  }
  .backdrop {
    position: absolute; inset: 0;
    background: linear-gradient(120deg, var(--paper-dark) 0%, var(--paper-light) 28%, var(--paper-mid) 55%, var(--paper-light) 80%, var(--paper-mid) 100%);
  }
  .title-frame { position: absolute; left: 0; top: 0; }
  .name {
    position: absolute; left: 0; top: 48px; width: 896px; text-align: center;
    white-space: nowrap;
    font-family: "Crimson Pro", Georgia, serif; font-weight: 700; font-size: 76px;
    letter-spacing: -2.5px; color: var(--blue); line-height: 1;
    transform: scaleX(0.88); transform-origin: 50% 50%;
  }
  .office {
    position: absolute; left: 248px; top: 145px; width: 400px; text-align: center;
    white-space: nowrap;
    font-family: "Crimson Pro", Georgia, serif; font-weight: 700; font-size: 42px;
    letter-spacing: -0.5px; color: var(--blue); line-height: 1;
  }
  .virtue { position: absolute; font-family: "Crimson Pro", Georgia, serif; font-weight: 700; color: var(--blue); line-height: 1; letter-spacing: -1px; white-space: nowrap; }
  .virtue--lead { left: 134px; top: 264px; font-size: 68px; }
  .virtue--second { left: 70px; top: 334px; font-size: 42px; }
  .virtue--third { left: 160px; top: 384px; font-size: 42px; }
  .portrait {
    position: absolute; left: 432px; top: 238px; width: 399px; height: 460px;
    background: radial-gradient(ellipse at 50% 40%, #d8d8d8 0%, #9c9c9c 55%, #6f6f6f 100%);
  }
  .bio { position: absolute; text-align: right; }
  .bio--origin { left: 62px; width: 352px; top: 450px; font-size: 17.2px; line-height: 22.4px; font-weight: 700; }
  .bio--service { left: 66px; width: 348px; top: 670px; font-size: 15.4px; line-height: 19px; }
  .bio--courtroom { left: 444px; width: 388px; top: 728px; font-size: 15.4px; line-height: 19px; }
  .bio strong { font-weight: 700; }
  .vote-reminder {
    position: absolute; left: 0; width: 896px; top: 990px; text-align: center;
    font-family: "Crimson Pro", Georgia, serif; font-style: italic; font-weight: 700;
    font-size: 34px; color: var(--blue); letter-spacing: -0.3px;
  }
  .thanks { position: absolute; left: 230px; width: 202px; top: 1046px; text-align: right; font-size: 17.5px; line-height: 22px; }
  .donate { position: absolute; left: 452px; top: 1051px; width: 138px; text-decoration: none; text-align: center; }
  .donate__button {
    display: block; height: 28px; border-radius: 14px;
    background: linear-gradient(var(--donate-top), var(--donate-bottom));
    color: #fff; font-family: "Roboto Condensed", Arial, sans-serif; font-weight: 700;
    font-size: 22px; line-height: 28px; letter-spacing: 0.5px;
  }
  .donate__note { display: block; font-family: "Roboto Condensed", Arial, sans-serif; font-size: 9px; color: var(--blue); margin-top: 1px; }
  .donate__provider { display: flex; align-items: center; justify-content: center; gap: 5px; margin-top: 1px; }
  .donate__name { font-family: "Crimson Text", Georgia, serif; font-weight: 700; font-size: 17px; color: var(--blue); }
  .donate__chip { width: 18px; height: 11px; background: #b9b9b9; border-radius: 2px; }
  .footer-band {
    position: absolute; left: 0; top: 1146px; width: 896px; height: 54px; background: var(--band);
    color: #fff; font-size: 13.5px; text-align: center; line-height: 54px; white-space: nowrap;
  }
</style>
</head>
<body>
<main class="page">
  <div class="backdrop" role="img" aria-label="Faded courthouse columns background"></div>

  <svg class="title-frame" width="896" height="200" aria-hidden="true">
    <polyline points="58,82 34,82 34,171 245,171" fill="none" stroke="#0d3a9e" stroke-width="3"/>
    <polyline points="844,82 868,82 868,171 658,171" fill="none" stroke="#0d3a9e" stroke-width="3"/>
  </svg>
  <h1 class="name">Maribel Catherine Van Horn</h1>
  <p class="office">for Circuit Court Judge</p>

  <p class="virtue virtue--lead">Dedicated</p>
  <p class="virtue virtue--second">Experienced</p>
  <p class="virtue virtue--third">Respected</p>

  <div class="portrait" role="img" aria-label="Portrait photo of the candidate"></div>

  <p class="bio bio--origin">She was born and raised in Tampa Florida, the daughter of an air-conditioning repairman who later opened his own successful business. As the first in her family to go to college, her parents could not have been more proud as she finished her degree at Gulf Coast University, then continued on to Capital State School of Law where she graduated with honors.</p>

  <p class="bio bio--service">Dedicating her life to public service in central Florida, she has spent the last 18 years as a prosecutor fighting for victims of child abuse and sexual abuse in Orange and Osceola counties. She participates in local charities such as the <strong>Harvest Table Pantry</strong> and the <strong>Open Pages Reading Circle</strong>. Maribel shares her knowledge and experience freely, often mentoring the other young prosecutors and lecturing on jury selection and trial strategies. She is also committed to ensuring ethical behavior in the profession of law. She is also committed to ensuring ethical behavior in the profession of law. In law school, she won an award for ethics and professionalism but since then she also served as <strong>Chair of a State Bar Grievance Committee</strong>, which handles complaints and ethical violations committed by local attorneys.</p>

  <p class="bio bio--courtroom">The cornerstone of Maribel’s candidacy for judge is her experience in the courtroom. Nobody knows how to run an efficient courtroom better than an attorney who has litigated a hundred felony jury trials and argued more pretrial motions than can be counted. But even a judge with all the right knowledge and experience cannot excel without the correct temperament. Ask any attorney or judge who has worked with Maribel and they will tell you that she treats everyone with respect and handles courtroom surprises with a calm head and sense of humor. She would love your support for judge and the opportunity to use her skills and experience to serve <strong>Orange and Osceola County</strong> in a new and exciting way.</p>

  <p class="vote-reminder">Remember to vote August 30, 2016!</p>

  <p class="thanks">Thank you very much for your contribution</p>
  <a class="donate" href="#">
    <span class="donate__button">DONATE</span>
    <span class="donate__note">Safe &amp; Secure</span>
    <span class="donate__provider"><span class="donate__name">CoinDrift</span><span class="donate__chip"></span></span>
  </a>

  <footer class="footer-band">Paid for by the Campaign to Elect Maribel Van Horn for Circuit Court Judge, Circuit 9, Group 14</footer>
</main>
</body>
</html>
```